Label design for our new range of organic honey.

We need a design for honey jars and tubs. The label needs to indicate we are located in the Western Australia. The design needs to be elegant, modern and attracting high end customers that focus on quality.

Need extra days to review

```html
<!DOCTYPE html>
<html lang="en">
<head>
<meta charset="utf-8">
<title>Redgum Grower's Honey – Jar Label</title>
<link rel="stylesheet" href="https://fonts.googleapis.com/css2?family=Josefin+Sans:wght@400&family=Montserrat:wght@400;600&display=swap">
<style>
  :root {
    --backdrop: #f4f4f4;
    --label-yellow: #f1d51c;
    --label-yellow-light: #f7e04a;
    --label-yellow-deep: #e6c712;
    --panel-black: #131313;
    --frame-line: #111111;
    --gold-text: #f0cf0a;
    --white-text: #f5f5f5;
    --honey-light: #f6c867;
    --honey-mid: #e3a93c;
    --honey-deep: #c9892a;
  }
  * { margin: 0; padding: 0; box-sizing: border-box; }
  html, body {
    width: 1200px; height: 1200px; overflow: hidden;
    background: var(--backdrop);
  }
  .canvas {
    position: relative; width: 1200px; height: 1200px;
  }
  .jar-label {
    position: absolute; left: 50px; top: 193px;
    width: 1100px; height: 814px;
    background: linear-gradient(100deg, var(--label-yellow-deep) 0%, var(--label-yellow) 35%, var(--label-yellow-light) 70%, var(--label-yellow) 100%);
    overflow: hidden;
  }
  .dipper-art {
    position: absolute; left: 99px; top: 204px;
    width: 250px; height: 596px;
    border-radius: 120px 120px 60px 60px;
    background: linear-gradient(180deg, var(--honey-mid) 0%, var(--honey-light) 45%, var(--honey-mid) 80%, var(--honey-deep) 100%);
    opacity: 0.85;
  }
  .brand-frame {
    position: absolute; left: 327px; top: 99px;
    width: 440px; height: 662px;
    border: 2px solid var(--frame-line);
  }
  .brand-panel {
    position: absolute; left: 16px; top: 16px; right: 16px; bottom: 16px;
    background: var(--panel-black);
    text-align: center;
  }
  .brand-mark {
    position: absolute; left: 50%; top: 40px;
    width: 150px; height: 150px; margin-left: -75px;
    border: 2px solid var(--white-text); border-radius: 50%;
  }
  .brand-name {
    position: absolute; left: 0; right: 0; top: 252px;
    font-family: 'Josefin Sans', sans-serif; font-weight: 400;
    color: var(--gold-text); text-transform: uppercase;
    line-height: 1.08;
  }
  .brand-name .line { display: block; font-size: 58px; letter-spacing: 0.5px; }
  .brand-name .line--product { font-size: 84px; letter-spacing: 2px; margin-top: 6px; }
  .origin {
    position: absolute; left: 0; right: 0; top: 558px;
    font-family: 'Montserrat', sans-serif; color: var(--white-text);
  }
  .origin__lead { display: block; font-size: 16px; font-weight: 400; letter-spacing: 0.3px; }
  .origin__region { display: block; font-size: 21px; font-weight: 600; letter-spacing: 0.5px; margin-top: 6px; }
  .net-volume {
    position: absolute; left: 0; right: 0; top: 775px;
    text-align: center;
    font-family: 'Montserrat', sans-serif; font-size: 15px; font-weight: 400;
    color: var(--frame-line);
  }
</style>
</head>
<body>
  <main class="canvas">
    <section class="jar-label">
      <div class="dipper-art" role="img" aria-label="Illustration of a wooden honey dipper with golden honey dripping into a pool"></div>
      <div class="brand-frame">
        <div class="brand-panel">
          <div class="brand-mark"></div>
          <h1 class="brand-name">
            <span class="line">Redgum</span>
            <span class="line">Grower’s</span>
            <span class="line line--product">Honey</span>
          </h1>
          <p class="origin">
            <span class="origin__lead">PRODUCT OF</span>
            <span class="origin__region">WESTERN AUSTRALIA</span>
          </p>
        </div>
      </div>
      <p class="net-volume">900 ML</p>
    </section>
  </main>
</body>
</html>
```